Solar Company Bussiness Card

I need a 2 sided business card and would like a .psd and any font files for each side of the card. I would like my logo used, it should be attached with the fonts. I'm not opposed to the font colors with the logo being changed.

On the sample design, I'd like the following:

Martin Halloway
President
Phone: 555-318-4907
www.brightvanepower.example

As I've recently opened in a 2nd market, I'm not sure about an address as I currently have 2 of them. I may actually get separate cards printed, one batch for each address, that's why I need the PSD file.
Updates

I'm very pleased with the response and designs I've received here for my business card. First and foremost, I'd like to thank everyone who took the time to submit a design. There truly are a lot of great designs in the bunch here and I'm having a little difficulty deciding. I will be reaching out to someone in the next day or two here to go to a final design. At this time, I'm not looking for any new concepts. If any of you do logos, I'm looking for a new logo for our sister entity, Halloway Partners, Inc. Thanks, Martin Halloway

Reason: I'm not looking for any new designs at this point, but extending this deadline in order to give people I've asked a chance to re-submit items.

Industry/Entity Type

Business

```html
<!DOCTYPE html>
<html lang="en">
<head>
<meta charset="utf-8">
<title>Brightvane Power – Business Card</title>
<link href="https://fonts.googleapis.com/css2?family=Exo+2:wght@400;500;600&display=swap" rel="stylesheet">
<style>
  :root {
    --page-bg: #e9e7e4;
    --card-white: #ffffff;
    --card-shade: #e4e5e7;
    --brand-blue: #1c5fa8;
    --band-deep: #2b45b3;
    --band-bright: #15a8e3;
    --swoosh-grey: #55585c;
    --ink: #2c2f33;
    --band-text: #ffffff;
  }
  * { margin: 0; padding: 0; box-sizing: border-box; }
  html, body { width: 1200px; height: 900px; overflow: hidden; }
  body {
    background: var(--page-bg);
    font-family: "Exo 2", sans-serif;
    display: flex;
    flex-direction: column;
    align-items: center;
    justify-content: center;
    gap: 56px;
  }
  .card {
    position: relative;
    width: 640px;
    height: 366px;
    background: radial-gradient(ellipse at 50% 45%, var(--card-white) 30%, var(--card-shade) 100%);
    box-shadow: 0 6px 18px rgba(0,0,0,0.18);
    overflow: hidden;
  }
  .card-band {
    position: absolute;
    left: 0; bottom: 0;
    width: 100%; height: 100%;
  }
  .brand {
    position: absolute;
    display: flex;
    align-items: center;
    gap: 10px;
    color: var(--brand-blue);
    font-weight: 500;
    letter-spacing: 0.5px;
    white-space: nowrap;
  }
  .brand-mark {
    background: var(--brand-blue);
    flex: none;
  }
  .card-front .brand { left: 40px; top: 70px; font-size: 28px; }
  .card-front .brand-mark { width: 18px; height: 18px; }
  .holder {
    position: absolute;
    left: 34px;
    bottom: 40px;
    color: var(--band-text);
  }
  .holder-name {
    font-size: 19px;
    font-weight: 500;
    letter-spacing: 1.5px;
    text-transform: uppercase;
  }
  .holder-title { font-size: 13px; margin-top: 2px; }
  .contact {
    position: absolute;
    left: 380px;
    top: 48px;
    width: 230px;
    color: var(--ink);
    font-size: 13px;
  }
  .contact-address {
    font-size: 15px;
    font-weight: 500;
    line-height: 1.35;
    margin-bottom: 22px;
    letter-spacing: 0.4px;
  }
  .contact-list { list-style: none; }
  .contact-list li {
    display: flex;
    align-items: center;
    gap: 10px;
    line-height: 1.75;
    letter-spacing: 0.3px;
    white-space: nowrap;
  }
  .contact-list svg { width: 12px; height: 12px; flex: none; fill: var(--brand-blue); }
  .card-back .brand {
    left: 50%; top: 50%;
    transform: translate(-50%, -50%);
    font-size: 40px;
  }
  .card-back .brand-mark { width: 26px; height: 26px; }
</style>
</head>
<body>

  <section class="card card-front" aria-label="Business card front">
    <svg class="card-band" viewBox="0 0 640 366" preserveAspectRatio="none" aria-hidden="true">
      <defs>
        <linearGradient id="bandGradient" x1="0" y1="0" x2="1" y2="0">
          <stop offset="0" stop-color="var(--band-deep)"/>
          <stop offset="0.55" stop-color="var(--band-bright)"/>
          <stop offset="1" stop-color="var(--band-deep)"/>
        </linearGradient>
        <linearGradient id="swooshGradient" x1="0" y1="0" x2="1" y2="0">
          <stop offset="0" stop-color="#d8d9db"/>
          <stop offset="0.6" stop-color="var(--swoosh-grey)"/>
          <stop offset="1" stop-color="#2f3235"/>
        </linearGradient>
      </defs>
      <path d="M0 262 C 150 250, 260 300, 360 300 C 460 300, 540 268, 640 300 L640 366 L0 366 Z" fill="url(#bandGradient)"/>
      <path d="M300 366 C 420 330, 540 318, 640 326 L640 366 Z" fill="url(#swooshGradient)"/>
      <path d="M330 366 C 440 340, 550 334, 640 340 L640 366 Z" fill="var(--band-deep)"/>
    </svg>

    <div class="brand">
      <span class="brand-mark" aria-hidden="true"></span>
      <span class="brand-name">Brightvane Power</span>
    </div>

    <div class="contact">
      <p class="contact-address">21 Crestline Ave, Suite 4<br>Riverside Park KLG</p>
      <ul class="contact-list">
        <li>
          <svg viewBox="0 0 12 12" aria-hidden="true"><path d="M2.5 0.5 L4.5 0.5 L5.2 3.2 L3.8 4.3 C4.4 5.8 6.2 7.6 7.7 8.2 L8.8 6.8 L11.5 7.5 L11.5 9.5 C11.5 10.6 10.6 11.5 9.5 11.5 C4.8 11.5 0.5 7.2 0.5 2.5 C0.5 1.4 1.4 0.5 2.5 0.5 Z"/></svg>
          <span>555-318-4907</span>
        </li>
        <li>
          <svg viewBox="0 0 12 12" aria-hidden="true"><path d="M3 0 H9 V12 H3 Z M4 1.5 V9 H8 V1.5 Z M5.4 10 H6.6 V11 H5.4 Z" fill-rule="evenodd"/></svg>
          <span>555-318-4907</span>
        </li>
        <li>
          <svg viewBox="0 0 12 12" aria-hidden="true"><path d="M0 2 H12 V10 H0 Z M1 3 V3.4 L6 6.6 L11 3.4 V3 Z" fill-rule="evenodd"/></svg>
          <span>martin@brightvanepower.example</span>
        </li>
        <li>
          <svg viewBox="0 0 12 12" aria-hidden="true"><path d="M6 0 A6 6 0 1 0 6 12 A6 6 0 1 0 6 0 Z M6 1 C7 2.2 7.5 4 7.5 6 C7.5 8 7 9.8 6 11 C5 9.8 4.5 8 4.5 6 C4.5 4 5 2.2 6 1 Z M1.2 5.5 H10.8 V6.5 H1.2 Z" fill-rule="evenodd"/></svg>
          <span>www.brightvanepower.example</span>
        </li>
      </ul>
    </div>

    <div class="holder">
      <p class="holder-name">Martin Halloway</p>
      <p class="holder-title">President</p>
    </div>
  </section>

  <section class="card card-back" aria-label="Business card back">
    <div class="brand">
      <span class="brand-mark" aria-hidden="true"></span>
      <span class="brand-name">Brightvane Power</span>
    </div>
  </section>

</body>
</html>
```